Keystone BRISK Repairs Business card

Keystone Motors is looking for a business card design for our detailing wing "Keystone BRISK Repairs"
The services offered are vehicle paintless dent repairs, vehicle detailing, scratch and bumper repairs & paint and alloy wheel repairs.
Ideally the card design should be sharp, neat and professional. We are not looking for a card with pictures of cars.
Our corporate colours are blues (as in the logo supplied) which may look good with water droplets in high res and perhaps one or two images leaking off the card. Dark blacks with electric blues perhaps.
Images may be of a spray gun (we use Torvanex), a rotary polisher (Quill WideStep) or similar objects used in the processes.

Industry/Entity Type

Paint

Contact Information for Business Card

Title: Keystone BRISK Repairs
Services: Bumper Repairs
Scratch/Paint Repairs
Paintless dent repairs
Alloy wheel repairs
Name: Martin K
Telephone: 0427195364
Email : martin@keystonemotors.com.au

Font styles to use
Sans Serif
Other font styles liked:

Colors
0355a3
3277b5
0792cd
cfdfed

Requirements
Must have
• The title - "Keystone BRISK Repairs" should be a focus on either the from or back of the card
Should not have
• Photographs of cars

```html
<!DOCTYPE html>
<html lang="en">
<head>
<meta charset="utf-8">
<title>Keystone BRISK Repairs – Business Card</title>
<link rel="stylesheet" href="https://fonts.googleapis.com/css2?family=Michroma&family=Questrial&display=swap">
<style>
  :root {
    --page: #f6f7f7;
    --navy: #0355a3;
    --steel: #3277b5;
    --cyan: #0792cd;
    --mist: #cfdfed;
    --ink: #1d1f5c;
    --white: #ffffff;
  }
  html, body {
    margin: 0;
    width: 1200px;
    height: 900px;
    overflow: hidden;
    background: var(--page);
  }
  .stage {
    position: relative;
    width: 1200px;
    height: 900px;
  }
  .card {
    position: absolute;
    top: 304px;
    width: 508px;
    height: 291px;
    box-shadow: 2px 3px 6px rgba(0,0,0,0.28);
    background: var(--white);
    overflow: hidden;
  }
  .card--front { left: 75px; }
  .card--back { left: 617px; }
  .card svg { display: block; }
  .fill-navy { fill: var(--navy); }
  .fill-steel { fill: var(--steel); }
  .fill-cyan { fill: var(--cyan); }
  .fill-mist { fill: var(--mist); }
  .fill-white { fill: var(--white); }
  .brand-name {
    font-family: "Questrial", sans-serif;
    font-size: 21px;
    fill: var(--ink);
    letter-spacing: 0.5px;
  }
  .brand-dot { fill: var(--ink); }
  .person-name {
    font-family: "Questrial", sans-serif;
    font-size: 19px;
    fill: var(--white);
    letter-spacing: 1px;
  }
  .person-title {
    font-family: "Questrial", sans-serif;
    font-size: 10px;
    fill: var(--white);
  }
  .contact-text {
    font-family: "Questrial", sans-serif;
    font-size: 11.5px;
    fill: var(--navy);
  }
  .tagline {
    font-family: "Michroma", sans-serif;
    font-size: 10.5px;
    fill: var(--navy);
  }
  .tagline-strong { font-weight: 700; }
</style>
</head>
<body>
<main class="stage">

  <section class="card card--front" aria-label="Business card front">
    <svg width="508" height="291" viewBox="0 0 508 291">
      <rect class="fill-steel" x="0" y="0" width="264" height="49"/>
      <rect class="fill-navy" x="0" y="195" width="264" height="48"/>
      <rect class="fill-mist" x="264" y="0" width="244" height="49"/>
      <rect class="fill-cyan" x="307" y="49" width="201" height="49"/>
      <rect class="fill-cyan" x="307" y="146" width="201" height="49"/>
      <rect class="fill-cyan" x="307" y="243" width="201" height="48"/>
      <rect class="fill-mist" x="263" y="49" width="44" height="242"/>
      <polygon class="fill-steel" points="263,0 307,49 307,98 263,49"/>
      <polygon class="fill-steel" points="307,146 307,195 263,243 263,195"/>
      <polygon class="fill-steel" points="263,243 307,243 307,291 263,291"/>
      <polygon class="fill-mist" points="263,243 307,243 263,291"/>

      <circle class="brand-dot" cx="52" cy="119" r="6"/>
      <text class="brand-name" x="66" y="127">Keystone Motors</text>

      <text class="person-name" x="224" y="219" text-anchor="end">MARTIN K</text>
      <text class="person-title" x="224" y="233" text-anchor="end">Director</text>

      <g class="contact">
        <rect class="fill-navy" x="316" y="203" width="13" height="13" rx="2"/>
        <path class="fill-white" d="M319.5 206c.6-.6 1.3-.5 1.7.1l.8 1.3c.3.5.1 1-.3 1.3l-.4.3c.5 1 1.2 1.7 2.2 2.2l.3-.4c.3-.4.8-.6 1.3-.3l1.3.8c.6.4.7 1.1.1 1.7l-.5.5c-2.8.5-6.8-3.5-6.3-6.3z"/>
        <text class="contact-text" x="335" y="214">0427195364</text>
        <rect class="fill-navy" x="316" y="221" width="13" height="13" rx="2"/>
        <rect class="fill-white" x="319" y="224.5" width="7" height="5.5"/>
        <polyline points="319,224.5 322.5,227.5 326,224.5" fill="none" stroke="#0355a3" stroke-width="0.8"/>
        <text class="contact-text" x="335" y="232" textLength="158" lengthAdjust="spacingAndGlyphs">martin@keystonemotors.com.au</text>
      </g>
    </svg>
  </section>

  <section class="card card--back" aria-label="Business card back">
    <svg width="509" height="291" viewBox="0 0 509 291">
      <rect class="fill-mist" x="0" y="0" width="245" height="49"/>
      <rect class="fill-cyan" x="0" y="49" width="201" height="49"/>
      <rect class="fill-cyan" x="0" y="146" width="201" height="49"/>
      <rect class="fill-cyan" x="0" y="243" width="201" height="48"/>
      <rect class="fill-steel" x="245" y="0" width="264" height="49"/>
      <rect class="fill-navy" x="245" y="195" width="264" height="48"/>
      <rect class="fill-mist" x="201" y="49" width="44" height="242"/>
      <polygon class="fill-steel" points="245,0 201,49 201,98 245,49"/>
      <polygon class="fill-steel" points="201,146 201,195 245,243 245,195"/>
      <polygon class="fill-steel" points="201,243 245,291 201,291"/>

      <text class="tagline" x="10" y="125" textLength="184" lengthAdjust="spacingAndGlyphs">Keystone <tspan class="tagline-strong">BRISK</tspan> Repairs</text>

      <circle class="brand-dot" cx="294" cy="119" r="6"/>
      <text class="brand-name" x="308" y="127">Keystone Motors</text>
    </svg>
  </section>

</main>
</body>
</html>
```